Advanced Therapeutic Massage Therapist

I need a business card advertising my massage services as an advanced therapeutic massage therapist. I offer advanced therapeutic massage, swedish and deep tissue. I want to create a simple, professional and feminine card. I like bright colours and creativity.

I prefer a bold and experimental approach rather than something status-quo. A card to suggest therapeutic healing through dynamic massage. Motifs, shapes or layout which suggest movement and flow.
Updates

Target Market(s)

Everybody!

Industry/Entity Type

Health And Wellness

Contact Information for Business Card

The card should include:
My name, logo, services offered and my contact details.

Aoibhín Delaney
Massage Therapist

- Swedish - Deep Tissue - Advanced Therapeutic

Phone: (+353) 87 261 9043
Email: regenerate@aoibhindelaney-example.com
Website: www.aoibhindelany-example.com

Font styles to use
Serif
Sans Serif
Decorative
Script

Colors

Designer to choose colors to be used in the design.

Requirements
Must have
• An example may contain something like this, yet concise:
• "Aoibhín Delaney
• Massage Therapist
• - Swedish - Deep Tissue - Advanced Therapeutic"
Nice to have
• This sentence is optional:
• Imagery such as a logo or symbol. I have attached a file containing a logo I had produced however the name is incorrect now as it is "Aoibhín" not "Evie". It could be edited to change it to Aoibhín.
• I have sent the file as .psd .jpg. .pdf and .png
• I like when the card conveys energy, movement, pressure points, flow etc.
• I just like the designer to follow their own style and ideas. I like bright colours but must have a lot of a base colour to offset it. I really prefer them to follow their own inspiration. That is my preference.
Should not have
• Pine trees, non-native trees to Britain and Ireland, exotic flowers or animals that are not native to Britain and Ireland.
• I don't like brown as the background colour of the card.
• The cars shouldn't look like a wedding invitation i.e too many floral type designs.

```html
<!DOCTYPE html>
<html lang="en">
<head>
<meta charset="utf-8">
<title>Aoibhín Delaney – Massage Therapist Business Card</title>
<link rel="stylesheet" href="https://fonts.googleapis.com/css2?family=Great+Vibes&family=Open+Sans:wght@400;600&family=Quicksand:wght@400;500&display=swap">
<style>
  :root {
    --backdrop: #2b2b2b;
    --card-white: #f4f4f4;
    --card-white-shade: #e9e9e9;
    --teal: #5cbfb2;
    --teal-deep: #49a99c;
    --teal-soft: #9fd9d1;
    --teal-top: #7ccbc0;
    --teal-bottom: #e4f4f2;
    --ink: #2f3436;
    --ink-soft: #3d4446;
  }
  * { margin: 0; padding: 0; box-sizing: border-box; }
  html, body {
    width: 1200px;
    height: 664px;
    overflow: hidden;
    background: var(--backdrop);
  }
  .card {
    position: absolute;
    top: 161px;
    width: 520px;
    height: 342px;
    overflow: hidden;
  }
  /* Front side */
  .card--front {
    left: 71px;
    background: linear-gradient(120deg, var(--card-white) 0%, #fbfbfb 45%, var(--card-white-shade) 100%);
  }
  .card--front .emblem {
    position: absolute;
    left: 335px;
    top: 23px;
    width: 148px;
    height: 148px;
    border-radius: 50%;
    background: radial-gradient(circle, var(--teal-soft) 0%, rgba(159,217,209,0.55) 55%, rgba(159,217,209,0.15) 100%);
  }
  .card--front .holder-name {
    position: absolute;
    left: 40px;
    top: 196px;
    font-family: "Great Vibes", cursive;
    font-size: 31px;
    color: var(--ink);
    line-height: 1;
  }
  .card--front .holder-role {
    position: absolute;
    left: 41px;
    top: 231px;
    font-family: "Quicksand", sans-serif;
    font-size: 11px;
    color: var(--teal);
    line-height: 1;
  }
  .card--front .divider {
    position: absolute;
    left: 41px;
    top: 255px;
    width: 437px;
    height: 2px;
    background: var(--teal);
  }
  .contact-row {
    position: absolute;
    left: 52px;
    top: 269px;
    display: flex;
    align-items: center;
    font-family: "Open Sans", sans-serif;
    font-size: 15px;
    color: var(--ink);
  }
  .contact-row .contact-item { display: flex; align-items: center; gap: 8px; }
  .contact-row .separator { margin: 0 24px 0 26px; font-size: 14px; }
  .contact-row svg { display: block; }
  /* Back side */
  .card--back {
    left: 627px;
    background: linear-gradient(180deg, var(--teal-top) 0%, #a9ddd6 55%, var(--teal-bottom) 100%);
  }
  .card--back .backdrop-motif {
    position: absolute;
    left: -98px;
    top: -14px;
    width: 370px;
    height: 370px;
    border-radius: 50%;
    background: radial-gradient(circle, rgba(255,255,255,0.22) 0%, rgba(255,255,255,0.14) 65%, rgba(255,255,255,0.04) 100%);
  }
  .card--back .emblem {
    position: absolute;
    left: 261px;
    top: 48px;
    width: 160px;
    height: 160px;
    border-radius: 50%;
    background: radial-gradient(circle, rgba(255,255,255,0.75) 0%, rgba(255,255,255,0.45) 60%, rgba(255,255,255,0.15) 100%);
  }
  .card--back .holder-name {
    position: absolute;
    left: 0;
    width: 694px;
    top: 206px;
    text-align: center;
    font-family: "Great Vibes", cursive;
    font-size: 31px;
    color: var(--ink);
    line-height: 1;
  }
  .card--back .holder-role {
    position: absolute;
    left: 0;
    width: 664px;
    top: 240px;
    text-align: center;
    font-family: "Quicksand", sans-serif;
    font-size: 11px;
    font-weight: 500;
    color: var(--ink-soft);
    line-height: 1;
  }
  .card--back .services {
    position: absolute;
    left: 0;
    width: 690px;
    top: 269px;
    text-align: center;
    font-family: "Open Sans", sans-serif;
    font-size: 13.5px;
    color: var(--ink);
    line-height: 1;
  }
</style>
</head>
<body>
  <section class="card card--front" aria-label="Business card front">
    <div class="emblem" role="img" aria-label="Tree of life emblem in a circle"></div>
    <p class="holder-name">Aoibhín Delaney</p>
    <p class="holder-role">Massage Therapist</p>
    <div class="divider"></div>
    <div class="contact-row">
      <span class="contact-item">
        <svg width="18" height="14" viewBox="0 0 18 14" aria-hidden="true">
          <path d="M1 4.5 C1 1.5 17 1.5 17 4.5 L17 6 L13 6 L13 4 L5 4 L5 6 L1 6 Z" fill="var(--teal-deep)"/>
          <path d="M4 7 L14 7 L16 13 L2 13 Z" fill="var(--teal-deep)"/>
          <circle cx="9" cy="10" r="1.8" fill="#f4f4f4"/>
        </svg>
        (+353) 87 261 9043
      </span>
      <span class="separator">I</span>
      <span class="contact-item">
        <svg width="18" height="13" viewBox="0 0 18 13" aria-hidden="true">
          <rect x="0.5" y="0.5" width="17" height="12" fill="var(--teal-deep)"/>
          <path d="M1 1 L9 7.5 L17 1" fill="none" stroke="#f4f4f4" stroke-width="1.3"/>
        </svg>
        aoibhinmassage@example.com
      </span>
    </div>
  </section>

  <section class="card card--back" aria-label="Business card back">
    <div class="backdrop-motif" role="img" aria-label="Large faint ornamental tree motif"></div>
    <div class="emblem" role="img" aria-label="Tree of life emblem in a circle"></div>
    <p class="holder-name">Aoibhín Delaney</p>
    <p class="holder-role">Massage Therapist</p>
    <p class="services">Swedish - Deep Tissue - Advanced Therapeutic</p>
  </section>
</body>
</html>
```